Upmarket Bathroom and Kitchen ware supplier needs a classy business card design

We are a company based in Fiji, we sell plumbing ware (Kitchen and bathroom taps, Basins,showers, toilets etc) through up market show rooms to individuals and directly through Architects and designers of resorts and holiday houses for new builds and renovations. we are wanting to upgrade our over all look and brand. we are starting with a new logo but will be rebranding the whole business. This project is for a business card design for my management and tales team I would like it to be dark, classy and interesting

Target Market(s)

Resort directors and Management, High end holiday home owners

Contact Information for Business Card

Gavin Threlkeld
Director
+64219473518

Colors

Designer to choose colors to be used in the design.

Requirements
Must have
• Must have an upmarket appearance I like darker charcoal shades but will be guided by the designers
• Please any catch phrases like "Crafting remarkable living rooms" this belongs tpo one of our suppliers so can not be used.
Nice to have
• Double sided, so front dedicated to logo provided and back info about the business and the person.

```html
<!DOCTYPE html>
<html lang="en">
<head>
<meta charset="utf-8">
<title>Lumora Interiors – Business Card</title>
<link rel="stylesheet" href="https://fonts.googleapis.com/css2?family=Raleway:wght@300;400&display=swap">
<style>
  :root {
    --backdrop: #2a2a2c;
    --card: #1c1c1d;
    --card-edge: #262628;
    --ink: #e9e9ea;
    --ink-soft: #a9a9ad;
    --rule: #8d8d92;
    --logo-ink: #5c5c60;
  }
  * { box-sizing: border-box; margin: 0; padding: 0; }
  html, body {
    width: 1200px;
    height: 800px;
    overflow: hidden;
    background: var(--backdrop);
    font-family: "Raleway", sans-serif;
  }
  .canvas {
    width: 1200px;
    height: 800px;
    display: flex;
    align-items: center;
    justify-content: center;
    gap: 48px;
  }
  .card {
    width: 532px;
    height: 304px;
    background: var(--card);
    border: 1px solid var(--card-edge);
    box-shadow: 0 18px 40px rgba(0, 0, 0, 0.45);
    position: relative;
  }

  /* Front: brand name */
  .card--front {
    display: flex;
    align-items: center;
    justify-content: center;
  }
  .brand {
    display: flex;
    align-items: center;
    gap: 24px;
  }
  .brand__dot {
    width: 14px;
    height: 14px;
    border-radius: 50%;
    background: var(--logo-ink);
  }
  .brand__words {
    display: flex;
    flex-direction: column;
    align-items: center;
    color: var(--logo-ink);
    font-weight: 300;
    text-transform: uppercase;
  }
  .brand__name {
    font-size: 28px;
    letter-spacing: 0.36em;
    padding: 0 0 6px 0.36em;
    border-bottom: 1px solid var(--logo-ink);
  }
  .brand__sub {
    margin-top: 6px;
    font-size: 11px;
    letter-spacing: 0.42em;
    padding-left: 0.42em;
  }

  /* Back: person and contact */
  .card--back {
    display: flex;
    flex-direction: column;
    align-items: center;
    justify-content: center;
    padding-top: 10px;
  }
  .person {
    display: flex;
    flex-direction: column;
    align-items: flex-end;
  }
  .person__name {
    color: var(--ink);
    font-weight: 400;
    font-size: 30px;
    letter-spacing: 0.06em;
    text-transform: uppercase;
    padding-bottom: 6px;
    border-bottom: 1px solid var(--rule);
  }
  .person__role {
    margin-top: 8px;
    color: var(--ink);
    font-weight: 400;
    font-size: 12px;
    letter-spacing: 0.32em;
    text-transform: uppercase;
    padding-right: 4px;
  }
  .contact {
    margin-top: 30px;
    display: flex;
    align-items: center;
    gap: 8px;
    color: var(--ink-soft);
    font-size: 13px;
    letter-spacing: 0.04em;
  }
  .contact__icon { width: 12px; height: 12px; }
  .tagline {
    margin-top: 34px;
    color: var(--ink-soft);
    font-size: 12px;
    letter-spacing: 0.04em;
    text-transform: uppercase;
  }
</style>
</head>
<body>
  <main class="canvas">
    <section class="card card--front" aria-label="Card front">
      <div class="brand">
        <span class="brand__dot"></span>
        <div class="brand__words">
          <span class="brand__name">Lumora</span>
          <span class="brand__sub">Interiors</span>
        </div>
      </div>
    </section>

    <section class="card card--back" aria-label="Card back">
      <div class="person">
        <h1 class="person__name">Gavin Threlkeld</h1>
        <p class="person__role">Director</p>
      </div>
      <p class="contact">
        <svg class="contact__icon" viewBox="0 0 24 24" aria-hidden="true">
          <path fill="#e9e9ea" d="M6.6 10.8a15.1 15.1 0 0 0 6.6 6.6l2.2-2.2a1 1 0 0 1 1-.25 11.4 11.4 0 0 0 3.6.57 1 1 0 0 1 1 1V20a1 1 0 0 1-1 1A17 17 0 0 1 3 4a1 1 0 0 1 1-1h3.5a1 1 0 0 1 1 1c0 1.25.2 2.45.57 3.57a1 1 0 0 1-.25 1z"/>
        </svg>
        <span class="contact__phone">+64219473518</span>
      </p>
      <p class="tagline">Curating refined bathroom spaces</p>
    </section>
  </main>
</body>
</html>
```